yard sign for lawncare business

I need a lawn sign design. ...The sign will be 18"X27"....it will be displayed with the 27" running horizontally. ...i need the company name and logo to be included and the same color as the graphic in the included file.....i also want the slogan included as well as the phone number 312-555-0186...all wording and numbers should be large and easy to see from passing cars on the road.....feel free to play around with background colors and wording and number placement

Ok guys....downloads are now available for viewing. ..sorry about the delay....thanks for your help and good luck

Business

```html
<!DOCTYPE html>
<html lang="en">
<head>
<meta charset="utf-8">
<title>TurfKeepers Yard Sign</title>
<link rel="stylesheet" href="https://fonts.googleapis.com/css2?family=Oswald:wght@700&family=Montserrat:wght@800&display=swap">
<style>
  :root {
    --page: #e9ecef;
    --frame: #c9ccd0;
    --leaf: #6cbf3f;
    --leaf-deep: #3f9a2a;
    --leaf-pale: #cfe8a6;
    --sky-tint: #dcecf6;
    --steel: #7d7e82;
    --ink: #111111;
    --white: #ffffff;
  }
  * { box-sizing: border-box; margin: 0; padding: 0; }
  html, body { width: 1200px; height: 1000px; overflow: hidden; background: var(--page); }
  .yard-sign {
    position: absolute; left: 50px; top: 133px;
    width: 1100px; height: 733px;
    border-radius: 28px;
    border: 6px solid var(--frame);
    overflow: hidden;
    background: linear-gradient(160deg, var(--sky-tint) 0%, var(--white) 30%, var(--white) 50%, var(--leaf-pale) 75%);
  }
  .accent-bar { position: absolute; top: 18px; height: 19px; }
  .accent-bar--green { left: 0; width: 140px; background: var(--leaf); clip-path: polygon(0 0, 100% 0, 88% 100%, 0 100%); }
  .accent-bar--grey { left: 158px; right: 0; background: var(--steel); clip-path: polygon(2% 0, 100% 0, 100% 100%, 0 100%); }
  .grass-art {
    position: absolute; left: 100px; top: 66px; width: 900px; height: 210px;
    border-radius: 50% 50% 0 0 / 90% 90% 0 0;
    background: linear-gradient(180deg, var(--leaf) 0%, #9ed35a 60%, rgba(207,232,166,0) 100%);
    opacity: .85;
  }
  .lawn-band {
    position: absolute; left: 0; right: 0; bottom: 0; height: 215px;
    background: linear-gradient(180deg, rgba(158,211,90,0) 0%, #9ed35a 35%, var(--leaf) 70%, var(--leaf-deep) 100%);
  }
  .brand-name {
    position: absolute; left: 0; right: 0; top: 296px;
    text-align: center;
    font-family: "Oswald", sans-serif; font-weight: 700;
    font-size: 150px; line-height: 150px; letter-spacing: 1px;
    color: var(--leaf);
  }
  .slogan {
    position: absolute; left: 0; right: 0; top: 480px;
    text-align: center;
    font-family: "Montserrat", sans-serif; font-weight: 800;
    font-size: 33px; color: var(--ink);
  }
  .phone-line {
    position: absolute; left: 70px; top: 540px;
    display: flex; align-items: center; gap: 16px;
  }
  .phone-icon { width: 110px; height: 110px; flex: none; }
  .phone-number {
    font-family: "Montserrat", sans-serif; font-weight: 800;
    font-size: 122px; line-height: 1; letter-spacing: -4px;
    color: var(--ink);
    -webkit-text-stroke: 6px var(--white); paint-order: stroke fill;
  }
</style>
</head>
<body>
  <div class="yard-sign">
    <div class="accent-bar accent-bar--green"></div>
    <div class="accent-bar accent-bar--grey"></div>
    <div class="grass-art" role="img" aria-label="Illustration of a tuft of tall green grass"></div>
    <div class="lawn-band" role="img" aria-label="Illustrated green grass along the bottom edge"></div>
    <h1 class="brand-name">TURFKEEPERS</h1>
    <p class="slogan">WHEN YOUR GRASS GETS TALL, GIVE US A CALL!</p>
    <div class="phone-line">
      <svg class="phone-icon" viewBox="0 0 110 110" aria-hidden="true">
        <circle cx="55" cy="55" r="51" fill="var(--leaf)" stroke="var(--white)" stroke-width="5"/>
        <path d="M36 30c4-3 8-2 10 2l5 9c2 3 1 6-2 8l-4 3c3 7 9 13 16 16l3-4c2-3 5-4 8-2l9 5c4 2 5 6 2 10l-4 5c-3 3-8 4-13 2-17-7-30-20-37-37-2-5-1-10 2-13z" fill="var(--ink)"/>
        <path d="M60 32a20 20 0 0 1 18 18M60 20a32 32 0 0 1 30 30" fill="none" stroke="var(--ink)" stroke-width="5" stroke-linecap="round"/>
      </svg>
      <span class="phone-number">312-555-0186</span>
    </div>
  </div>
</body>
</html>
```